Relocation/furniture installation company needs new business cards

we are a relocation and furniture installation company mainly dealing with corporate clients and we are looking for new business card ideas. Cards should incorporate our logo and list our website, phone number and services. The company is only 2 years old but with more staff joining we are in the need for more business cards, so something with an awesome design that is eye catching would go a long way to insure we get our name out there and look good to potential new clients.

Target Market(s)

Corporate

Industry/Entity Type

Trade

Contact Information for Business Card

www.mervoline.co.nz
0508 4 bravok

furniture installation
business relocations
joinery installation
commercial property maintenance

Colors
0592cd
34a7d8
85cae6
85acd3
0356a4
cfdfed
cee9f5
757575
474747

Requirements
Must have
• Business relocations and furniture installation specialists
Nice to have
• something that incorporates our logo.

```html
<!DOCTYPE html>
<html lang="en">
<head>
<meta charset="utf-8">
<title>Mervoline Business Cards</title>
<link href="https://fonts.googleapis.com/css2?family=Open+Sans:wght@400;600&family=Saira:wght@700&display=swap" rel="stylesheet">
<style>
  :root{
    --backdrop:#676767;
    --card:#f7f7f5;
    --navy:#2d3791;
    --sky:#1aa6dc;
    --steel:#3569a3;
    --white:#ffffff;
  }
  *{margin:0;padding:0;box-sizing:border-box}
  html,body{width:1200px;height:1011px;overflow:hidden}
  body{background:var(--backdrop);position:relative;font-family:"Open Sans",sans-serif;color:var(--navy)}
  .card{position:absolute;left:357px;width:486px;height:293px;background:var(--card);overflow:hidden}
  .card-front{top:186px}
  .card-back{top:532px}
  .brand{position:absolute;display:flex;align-items:center;gap:10px;font-family:"Saira",sans-serif;font-weight:700;color:var(--navy);letter-spacing:2px;white-space:nowrap}
  .brand-mark{width:14px;height:14px;background:var(--navy)}
  .card-front .brand{left:50%;top:118px;transform:translateX(-50%);font-size:38px}
  .card-front .brand-mark{width:18px;height:18px}
  .site-rule{position:absolute;left:0;top:270px;width:486px;height:12px}
  .site-url{position:absolute;left:0;width:486px;top:265px;text-align:center;font-size:12px;letter-spacing:2.4px;color:var(--navy)}
  .site-url span{color:var(--sky)}
  .person-name{position:absolute;left:31px;top:49px;font-family:"Saira",sans-serif;font-weight:700;font-size:25px;letter-spacing:1px}
  .person-role{position:absolute;left:31px;top:79px;font-size:13px}
  .card-back .brand{right:18px;top:100px;font-size:28px}
  .contacts{position:absolute;left:31px;top:158px;list-style:none}
  .contacts li{display:flex;align-items:center;height:19.5px;font-size:13px}
  .contacts svg{width:11px;height:11px;margin-right:12px;fill:var(--sky)}
  .waves{position:absolute;left:0;top:0;width:486px;height:293px}
  .services{position:absolute;right:17px;top:216px;list-style:none;text-align:right;color:var(--white);font-size:12.5px;line-height:15.2px}
  .services li::after{content:"«";color:#85cae6;margin-left:8px;font-size:11px}
</style>
</head>
<body>
  <section class="card card-front">
    <div class="brand"><span class="brand-mark"></span>MERVOLINE</div>
    <svg class="site-rule" viewBox="0 0 486 12" aria-hidden="true">
      <polygon points="30,6 148,3 148,9" fill="var(--navy)"/>
      <polygon points="456,6 338,3 338,9" fill="var(--navy)"/>
    </svg>
    <p class="site-url">www.<span>mervoline</span>.co.nz</p>
  </section>

  <section class="card card-back">
    <h1 class="person-name">AARON WHITBY</h1>
    <p class="person-role">Managing Director</p>
    <div class="brand"><span class="brand-mark"></span>MERVOLINE</div>
    <ul class="contacts">
      <li><svg viewBox="0 0 12 12"><path d="M1 5c0-2 2-3 5-3s5 1 5 3H8.5V4h-5v1zM2 6h8l1 5H1z"/></svg>0508 4 bravok</li>
      <li><svg viewBox="0 0 12 12"><path d="M0 2h12v8H0zM1 3l5 4 5-4v6H1z" fill-rule="evenodd"/></svg>aaron@mervoline.co.nz</li>
      <li><svg viewBox="0 0 12 12"><circle cx="6" cy="6" r="5.5"/><path d="M0.5 6h11M6 .5v11M2 3h8M2 9h8" stroke="#f7f7f5" stroke-width=".8" fill="none"/></svg>www.mervoline.co.nz</li>
    </ul>
    <svg class="waves" viewBox="0 0 486 293" aria-hidden="true">
      <path d="M240 240 C330 200 400 150 486 153 L486 160 C400 160 330 210 250 244 Z" fill="var(--sky)"/>
      <path d="M0 265 C120 310 200 280 300 240 C380 205 430 172 486 170 L486 293 L0 293 Z" fill="var(--navy)"/>
      <path d="M0 236 C60 265 130 268 250 240 C140 275 70 275 0 255 Z" fill="var(--steel)"/>
      <path d="M40 247 C110 262 180 262 250 240 C180 262 110 265 40 250 Z" fill="var(--steel)"/>
    </svg>
    <ul class="services">
      <li>Joinery Installation</li>
      <li>Furniture Installation</li>
      <li>Business Relocations</li>
      <li>Commercial Property Maintenance</li>
    </ul>
  </section>
</body>
</html>
```